Brisco Energy PowerPoint Design

Looking for a sleek PowerPoint design for our energy services company. We supply EV charging, Solar, Battery Storage and more.

Please make the background white with hints of gray and utilize the exact dark blue and light blue colors in the logo.

This design should be sharp with minimal round edges.

Colors

Designer to choose colors to be used in the design.

```html
<!DOCTYPE html>
<html lang="en">
<head>
<meta charset="utf-8">
<title>Brisco Energy Presentation Slides</title>
<link href="https://fonts.googleapis.com/css2?family=Poppins:ital,wght@0,400;0,500;0,600;0,700;0,800;1,500&family=Open+Sans:ital,wght@0,400;0,600;1,400&family=Oswald:wght@600;700&family=Roboto+Condensed:wght@700&display=swap" rel="stylesheet">
<style>
:root{
  --navy:#1f1668;
  --navy-deep:#18115a;
  --blue:#3fb3ee;
  --ink:#4a4a58;
  --soft:#f1f2f4;
  --line:#c9cbd3;
  --stage:#dddee1;
}
*{box-sizing:border-box;margin:0;padding:0}
html,body{width:900px;height:1200px;overflow:hidden;background:var(--stage)}
.canvas{position:relative;width:900px;height:1200px;overflow:hidden;background:var(--stage)}
.slide{position:absolute;width:491px;height:276px;transform:scale(.5425);transform-origin:0 0;background:#fff;overflow:hidden;font-family:'Open Sans',sans-serif;color:var(--ink);box-shadow:0 4px 10px rgba(0,0,0,.25)}
.c1{left:38px}.c2{left:317px}.c3{left:596px}
.r1{top:39px}.r2{top:201px}.r3{top:363px}.r4{top:523px}.r5{top:685px}.r6{top:847px}.r7{top:1009px}
.abs{position:absolute}
.ttl{position:absolute;left:22px;top:10px;font:600 16px/1.2 'Poppins',sans-serif;color:var(--navy)}
.ttl::after{content:"";display:block;width:12px;height:2px;background:var(--blue);margin-top:4px;box-shadow:15px 0 0 -0.5px var(--navy)}
.logo{position:absolute;right:12px;top:10px;font:700 7px 'Poppins',sans-serif;color:var(--navy);display:flex;align-items:center;gap:3px}
.logo::before{content:"";width:7px;height:7px;background:var(--navy)}
.foot{position:absolute;left:0;right:0;top:250px;height:10px}
.foot .rule{position:absolute;left:36px;right:14px;top:5px;height:.6px;background:var(--navy)}
.foot .cr{position:absolute;left:14px;top:2px;font:600 3px 'Poppins',sans-serif;color:var(--navy);background:#fff;padding-right:2px}
.foot .pg{position:absolute;right:8px;top:2px;font:4px 'Open Sans',sans-serif;color:var(--navy);background:#fff;padding:0 2px}
.p{font-size:4px;line-height:1.45;color:#666}
.h{font:600 6px 'Poppins',sans-serif;color:var(--navy)}
.hb{font:600 6px 'Poppins',sans-serif;color:var(--blue)}
.photo{position:absolute}
.dot{position:absolute;border-radius:50%;background:var(--blue);display:flex;align-items:center;justify-content:center}
.box{position:absolute}
</style>
</head>
<body>
<div class="canvas">

<!-- 1 cover -->
<section class="slide c1 r1">
  <div class="photo" role="img" aria-label="Faded photo of a solar carport over parked cars" style="inset:0;background:linear-gradient(180deg,#e9eaee 0%,#f5f5f7 60%,#eceef1 100%)"></div>
  <div class="abs" style="left:0;right:0;top:95px;text-align:center;font:700 34px 'Poppins',sans-serif;color:var(--navy)">Brisco Energy</div>
  <div class="abs" style="left:0;right:0;top:198px;text-align:center;font:700 19px 'Roboto Condensed',sans-serif;color:#12103a">COMPANY BUSINESS MARKETING</div>
  <div class="abs" style="left:0;right:0;top:229px;height:1px;background:var(--blue)"></div>
  <div class="abs" style="left:175px;top:225px;width:140px;background:#f4f5f7;text-align:center;font:600 7px 'Open Sans',sans-serif;letter-spacing:2.5px;color:#222">www.<span style="color:var(--blue)">website</span>.com</div>
</section>

<!-- 2 title -->
<section class="slide c2 r1">
  <div class="abs" style="left:0;top:0;width:206px;height:276px;background:linear-gradient(180deg,#fff,#f3f4f6)"></div>
  <div class="abs" style="left:11px;top:9px;width:7px;height:7px;background:var(--blue)"></div>
  <div class="abs" style="left:36px;top:45px;font:700 14px 'Poppins',sans-serif;color:var(--navy)">Brisco Energy</div>
  <div class="abs" style="left:27px;top:108px;font:700 37px/1 'Oswald',sans-serif;color:var(--navy-deep)">BUSINESS</div>
  <div class="abs" style="left:28px;top:153px;font:600 16px 'Poppins',sans-serif;letter-spacing:1px;color:var(--blue)">MARKETING</div>
  <div class="abs" style="left:28px;top:183px;width:10px;height:2px;background:var(--blue);box-shadow:13px 0 0 var(--navy)"></div>
  <div class="abs" style="left:28px;top:190px;font:italic 500 9px 'Poppins',sans-serif;color:#222">Presentation</div>
  <div class="abs p" style="left:28px;top:204px;width:110px;font-style:italic">Lorem ipsum dolor sit amet, consectetur adipiscing elit, sed diam nonum</div>
  <div class="abs" style="left:29px;top:238px;display:flex;gap:5px"><i style="width:4px;height:4px;border-radius:50%;background:var(--navy)"></i><i style="width:4px;height:4px;border-radius:50%;background:var(--blue)"></i><i style="width:4px;height:4px;border-radius:50%;background:var(--navy)"></i></div>
  <div class="photo" role="img" aria-label="Photo of a man using his phone beside an electric car at a charging station" style="left:206px;top:0;width:285px;height:222px;background:linear-gradient(135deg,#9fb6cf 0%,#6f7f90 45%,#3b4048 100%)"></div>
  <div class="abs" style="left:206px;top:222px;width:285px;height:54px;background:var(--navy-deep);color:#fff;font:500 8px 'Poppins',sans-serif;letter-spacing:3px;text-align:center;padding-top:22px">WWW.WEBSITE.COM</div>
</section>

<!-- 3 agenda -->
<section class="slide c3 r1">
  <div class="logo">Brisco Energy</div>
  <div class="abs" style="left:74px;top:105px;font:700 30px 'Poppins',sans-serif;color:#12103a">Agenda</div>
  <div class="abs" style="left:238px;top:50px;width:190px">
    <div class="hb" style="font-size:8px;font-weight:500">1. Lorem ipsum</div><p class="p" style="margin:2px 0 17px 12px">Lorem ipsum dolor sit amet, consectetuer adipiscing elit, sed diam nonummy nibh euismod tincid</p>
    <div class="hb" style="font-size:8px;font-weight:500">2. Lorem ipsum</div><p class="p" style="margin:2px 0 17px 12px">Lorem ipsum dolor sit amet, consectetuer adipiscing elit, sed diam nonummy nibh euismod tincid</p>
    <div class="hb" style="font-size:8px;font-weight:500">3. Lorem ipsum</div><p class="p" style="margin:2px 0 17px 12px">Lorem ipsum dolor sit amet, consectetuer adipiscing elit, sed diam nonummy nibh euismod tincid</p>
    <div class="hb" style="font-size:8px;font-weight:500">4. Lorem ipsum</div><p class="p" style="margin:2px 0 0 12px">Lorem ipsum dolor sit amet, consectetuer adipiscing elit, sed diam nonummy nibh euismod tincid</p>
  </div>
  <div class="foot"><div class="rule"></div><span class="cr">BE © Brisco Energy. All rights reserved</span><span class="pg">2</span></div>
</section>

<!-- 4 -->
<section class="slide c1 r2">
  <div class="logo">Brisco Energy</div>
  <div class="abs" style="left:22px;top:12px;font:700 15px/1.25 'Poppins',sans-serif;color:var(--navy)">Lorem Ipsum<br>Dolor Sit<br>Ametkeeper.</div>
  <div class="abs" style="left:22px;top:80px;width:12px;height:2px;background:var(--blue);box-shadow:15px 0 0 var(--navy)"></div>
  <div class="abs p" style="left:22px;top:92px;width:122px;text-align:justify">Lorem ipsum dolor sit amet, consectetuer adipiscing elit, sed diam nonummy nibh euismod tincidunt ut laoreet dolore magna aliquam erat volutpat.<br><br>Ut wisi enim ad minim veniam, quis nostrud exerci tation ullamcorper suscipit lobortis nisl ut aliquip ex ea commodo consequat. Duis autem vel eum iriure dolor in hendrerit in vulputate velit esse molestie consequat.<br><br>vel illum dolore eu feugiat nulla facilisis at vero eros et accumsan et iusto odio</div>
  <div class="photo" role="img" aria-label="Aerial photo of a solar carport with EV chargers and parked cars" style="left:170px;top:47px;width:321px;height:118px;background:linear-gradient(160deg,#7e8fa3,#4d6075 50%,#9aa4ad)"></div>
  <div class="abs" style="left:193px;top:150px;width:74px;height:95px;background:#fff;box-shadow:0 1px 3px rgba(0,0,0,.2)"><div style="background:var(--blue);color:#fff;font:500 8px 'Poppins',sans-serif;padding:3px 5px">Text Here</div><p class="p" style="padding:4px 5px;font-size:3.3px">Lorem ipsum dolor sit amet, consectetuer adipiscing elit, sed diam nonummy nibh euismod tincidunt ut laoreet dolore magna aliquam erat volutpat.<br><br>Ut wisi enim ad minim veniam, quis nostrud exerci tation ullamcorper suscipit lobortis nisl ut aliquip ex ea commodo conse</p></div>
  <div class="abs" style="left:293px;top:150px;width:74px;height:95px;background:#fff;box-shadow:0 1px 3px rgba(0,0,0,.2)"><div style="background:var(--blue);color:#fff;font:500 8px 'Poppins',sans-serif;padding:3px 5px">Text Here</div><p class="p" style="padding:4px 5px;font-size:3.3px">Lorem ipsum dolor sit amet, consectetuer adipiscing elit, sed diam nonummy nibh euismod tincidunt ut laoreet dolore magna aliquam erat volutpat.<br><br>Ut wisi enim ad minim veniam, quis nostrud exerci tation ullamcorper suscipit lobortis nisl ut aliquip ex ea commodo conse</p></div>
  <div class="abs" style="left:393px;top:150px;width:74px;height:95px;background:#fff;box-shadow:0 1px 3px rgba(0,0,0,.2)"><div style="background:var(--blue);color:#fff;font:500 8px 'Poppins',sans-serif;padding:3px 5px">Text Here</div><p class="p" style="padding:4px 5px;font-size:3.3px">Lorem ipsum dolor sit amet, consectetuer adipiscing elit, sed diam nonummy nibh euismod tincidunt ut laoreet dolore magna aliquam erat volutpat.<br><br>Ut wisi enim ad minim veniam, quis nostrud exerci tation ullamcorper suscipit lobortis nisl ut aliquip ex ea commodo conse</p></div>
  <div class="foot"><div class="rule"></div><span class="cr">BE © Brisco Energy. All rights reserved</span><span class="pg">3</span></div>
</section>

<!-- 5 -->
<section class="slide c2 r2">
  <div class="ttl">Text Added Hare</div><div class="logo">Brisco Energy</div>
  <div class="photo" role="img" aria-label="Faint world map in the background" style="left:70px;top:40px;width:350px;height:160px;background:radial-gradient(ellipse at center,#f2f3f6 0%,#fff 70%)"></div>
  <svg class="abs" style="left:90px;top:58px" width="320" height="132" viewBox="0 0 320 132">
    <g fill="none" stroke="var(--navy)" stroke-width="2.5">
      <path d="M8 5h70v28 M8 5v118h60l10-10V33"/>
      <path d="M122 5h70v28 M122 5v96l-10 10v12h80V33"/>
      <path d="M236 5h70v118h-70V33"/>
      <path d="M78 33 112 111 M192 33 236 33"/>
    </g>
    <g fill="var(--navy)"><circle cx="78" cy="33" r="3.5"/><circle cx="192" cy="33" r="3.5"/></g>
    <g font-family="Poppins,sans-serif" font-size="7" font-weight="600" fill="var(--blue)" text-anchor="middle">
      <text x="43" y="50">IDEA</text><text x="157" y="50">PROMOTION</text><text x="271" y="50">GROWTH</text>
    </g>
    <g fill="none" stroke="var(--blue)" stroke-width="1"><circle cx="43" cy="32" r="4"/><rect x="151" y="29" width="12" height="8"/><path d="M265 38h12M266 36l4-4 3 2 4-5"/></g>
    <g font-family="Open Sans,sans-serif" font-size="3.6" fill="#666" text-anchor="middle">
      <text x="43" y="62">Lorem ipsum dolor sit amet,</text><text x="43" y="67">consectetuer adipiscing elit,</text><text x="43" y="72">sed diam nonummy nibh</text><text x="43" y="77">euismod tincidunt ut</text><text x="43" y="82">laoreet dolore magna</text><text x="43" y="87">aliquam erat volutpat. Ut</text><text x="43" y="92">wisi enim ad minim veniam,</text><text x="43" y="97">quis nostrud exerci tation</text><text x="43" y="102">ullamcorper suscipit lobortis</text>
      <text x="157" y="62">Lorem ipsum dolor sit amet,</text><text x="157" y="67">consectetuer adipiscing elit,</text><text x="157" y="72">sed diam nonummy nibh</text><text x="157" y="77">euismod tincidunt ut</text><text x="157" y="82">laoreet dolore magna</text><text x="157" y="87">aliquam erat volutpat. Ut</text><text x="157" y="92">wisi enim ad minim veniam,</text><text x="157" y="97">quis nostrud exerci tation</text><text x="157" y="102">ullamcorper suscipit lobortis</text>
      <text x="271" y="62">Lorem ipsum dolor sit amet,</text><text x="271" y="67">consectetuer adipiscing elit,</text><text x="271" y="72">sed diam nonummy nibh</text><text x="271" y="77">euismod tincidunt ut</text><text x="271" y="82">laoreet dolore magna</text><text x="271" y="87">aliquam erat volutpat. Ut</text><text x="271" y="92">wisi enim ad minim veniam,</text><text x="271" y="97">quis nostrud exerci tation</text><text x="271" y="102">ullamcorper suscipit lobortis</text>
    </g>
  </svg>
  <p class="abs p" style="left:60px;top:202px;width:372px;text-align:center">Lorem ipsum dolor sit amet, consectetuer adipiscing elit, sed diam nonummy nibh euismod tincidunt ut laoreet dolore magna aliquam erat volutpat. Ut wisi enim ad minim veniam, quis nostrud exerci tation ullamcorper suscipit lobortis nisl ut aliquip ex ea commodo consequat. Duis autem vel eum iriure dolor in hendrerit i</p>
  <div class="foot"><div class="rule"></div><span class="cr">BE © Brisco Energy. All rights reserved</span><span class="pg">4</span></div>
</section>

<!-- 6 -->
<section class="slide c3 r2">
  <div class="ttl">Text Added Hare</div><div class="logo">Brisco Energy</div>
  <div class="abs" style="left:55px;top:62px;width:200px">
    <div class="h">01. Aliquam Erat Volutpat</div><p class="p" style="margin:2px 0 14px 12px">Lorem ipsum dolor sit amet, consectetuer adipiscing elit, sed diam nonummy nibh euismod</p>
    <div class="h">02. Consectetuer Adipiscing Elit</div><p class="p" style="margin:2px 0 14px 12px">Lorem ipsum dolor sit amet, consectetuer adipiscing elit, sed diam nonummy nibh euismod tincidunt ut laoreet</p>
    <div class="h">03. Duis Autem Vel Eum</div><p class="p" style="margin:2px 0 14px 12px">Lorem ipsum dolor sit amet, consectetuer adipiscing elit, sed diam nonummy nibh euismod tincidunt.</p>
    <div class="h">04. Aliquam Erat Volutpat</div><p class="p" style="margin:2px 0 0 12px">Lorem ipsum dolor sit amet, consectetuer adipiscing elit, sed diam nonummy nibh euismod tincidunt ut laoreet.</p>
  </div>
  <div class="abs" style="left:270px;top:58px;width:170px;height:171px;background:var(--navy-deep)"></div>
  <div class="dot" style="left:250px;top:80px;width:28px;height:28px;border:3px solid #fff"></div>
  <div class="dot" style="left:250px;top:128px;width:28px;height:28px;border:3px solid #fff"></div>
  <div class="dot" style="left:250px;top:176px;width:28px;height:28px;border:3px solid #fff"></div>
  <div class="abs" style="left:300px;top:80px;width:130px;color:#fff"><div style="font:500 8px 'Poppins',sans-serif;color:var(--blue)">Lorem ipsum</div><p style="font-size:4px;line-height:1.4">ipsum dolor sit amet, cons ectetuer adipiscing elit, sed diam nonummy</p></div>
  <div class="abs" style="left:300px;top:128px;width:130px;color:#fff"><div style="font:500 8px 'Poppins',sans-serif;color:var(--blue)">Lorem ipsum</div><p style="font-size:4px;line-height:1.4">ipsum dolor sit amet, cons ectetuer adipiscing elit, sed diam nonummy nibh euismod tincidunt ut laoreet</p></div>
  <div class="abs" style="left:300px;top:178px;width:130px;color:#fff"><div style="font:500 8px 'Poppins',sans-serif;color:var(--blue)">Lorem ipsum</div><p style="font-size:4px;line-height:1.4">ipsum dolor sit amet, cons ectetuer adipiscing elit, sed diam nonummy</p></div>
  <div class="foot"><div class="rule"></div><span class="cr">BE © Brisco Energy. All rights reserved</span><span class="pg">5</span></div>
</section>

<!-- 7 -->
<section class="slide c1 r3">
  <div class="ttl">Text Added Hare</div><div class="logo">Brisco Energy</div>
  <p class="abs p" style="left:22px;top:55px;width:95px;font-size:4.6px">Lorem ipsum dolor sit amet,consectetuer adipiscing elit, sed diam nonummy nibh euismod tincidunt erat volutpat.<br><br>Ut wisi enim ad minim veniam, quis nostrud exerci tation ullamcorper suscipit lobortis nisl ut aliquip ex ea commodo-consequat.<br><br>quis nostrud exerci do tation ullamcorper suscipit lobortis consequat.</p>
  <div class="photo" role="img" aria-label="Collage of wind turbines, solar panels and an electric car" style="left:112px;top:30px;width:180px;height:220px;clip-path:polygon(40% 0,100% 0,60% 100%,0 100%);background:linear-gradient(180deg,#6fb9ea 0%,#3c7bc4 45%,#2a2c86 100%)"></div>
  <div class="dot" style="left:232px;top:60px;width:24px;height:24px;background:#fff;border:2px solid var(--blue)"><i style="width:10px;height:8px;background:var(--navy);border-radius:4px 4px 1px 1px"></i></div>
  <div class="dot" style="left:215px;top:118px;width:24px;height:24px;background:#fff;border:2px solid var(--blue)"><i style="width:9px;height:9px;background:var(--navy)"></i></div>
  <div class="dot" style="left:197px;top:175px;width:24px;height:24px;background:#fff;border:2px solid var(--blue)"><i style="width:9px;height:7px;background:var(--navy);border-radius:4px 4px 0 0"></i></div>
  <div class="abs" style="left:305px;top:60px;width:150px"><div class="hb" style="font-size:7px">We Before Me</div><p class="p">ipsum dolor sit amet, cons ectetuer adipiscing elit, sed diam nonummy nibh euismod tincidunt ut laoreet</p></div>
  <div class="abs" style="left:278px;top:118px;width:160px"><div class="hb" style="font-size:7px">We Are Good People</div><p class="p">ipsum dolor sit amet, cons ectetuer adipiscing elit, sed diam nonummy nibh euismod tincidunt ut laoreet dolore magna aliquam erat volutpat.</p></div>
  <div class="abs" style="left:248px;top:178px;width:160px"><div class="hb" style="font-size:7px">We Work with Heart</div><p class="p">ipsum dolor sit amet, cons ectetuer adipiscing elit, sed diam nonummy nibh euismod tincidunt</p></div>
  <div class="foot"><div class="rule"></div><span class="cr">BE © Brisco Energy. All rights reserved</span><span class="pg">6</span></div>
</section>

<!-- 8 section break -->
<section class="slide c2 r3">
  <div class="abs" style="left:22px;top:18px;width:446px;height:238px;background:var(--navy)"></div>
  <div class="photo" role="img" aria-label="Faint photo of a carport behind a dark blue overlay" style="left:22px;top:100px;width:446px;height:156px;background:linear-gradient(180deg,rgba(31,22,104,0) 0%,rgba(60,60,140,.5) 100%)"></div>
  <div class="abs" style="left:124px;top:72px;width:207px;height:120px;border:1.5px solid var(--blue)"></div>
  <div class="abs" style="left:270px;top:52px;width:64px;height:62px;background:var(--blue);color:#fff;font:700 36px/62px 'Oswald',sans-serif;text-align:center">01</div>
  <div class="abs" style="left:130px;top:78px;background:var(--navy);padding:0 4px;color:#fff;font:600 27px/1 'Poppins',sans-serif">Section<br>Break</div>
  <p class="abs" style="left:133px;top:143px;width:180px;color:#fff;font-size:8px;line-height:1.3">Lorem ipsum dolor sit amet, consectetuer sed diam nonummy euismod tincid</p>
</section>

<!-- 9 -->
<section class="slide c3 r3">
  <div class="ttl">Text Added Hare</div><div class="logo">Brisco Energy</div>
  <div class="photo" role="img" aria-label="Photo of workers installing a solar panel on a roof" style="left:70px;top:57px;width:145px;height:170px;background:linear-gradient(170deg,#c7ccd3 0%,#8c9198 50%,#4c5058 100%)"></div>
  <div class="abs" style="left:95px;top:208px;width:76px;height:20px;background:var(--navy-deep);color:#fff;font:600 10px/20px 'Poppins',sans-serif;text-align:center">Service</div>
  <div class="dot" style="left:238px;top:62px;width:22px;height:22px"><i style="width:10px;height:10px;border:1.5px solid #fff;border-radius:50%"></i></div>
  <div class="dot" style="left:238px;top:124px;width:22px;height:22px"><i style="width:10px;height:10px;border:1.5px solid #fff;border-radius:50%"></i></div>
  <div class="dot" style="left:238px;top:186px;width:22px;height:22px"><i style="width:10px;height:10px;border:1.5px solid #fff;border-radius:50%"></i></div>
  <div class="abs" style="left:287px;top:60px;width:160px"><div class="h" style="font-size:7.5px">Project name</div><p class="p">Lorem ipsum dolor sit amet, nec an dictas equidem appellantur, ut has commune accommodare. Mea illum, ludus solet idpro.</p></div>
  <div class="abs" style="left:287px;top:122px;width:160px"><div class="h" style="font-size:7.5px">Project name</div><p class="p">Lorem ipsum dolor sit amet, nec an dictas equidem appellantur, ut has commune accommodare. Mea illum, ludus solet idpro.</p></div>
  <div class="abs" style="left:287px;top:184px;width:160px"><div class="h" style="font-size:7.5px">Project name</div><p class="p">Lorem ipsum dolor sit amet, nec an dictas equidem appellantur, ut has commune accommodare. Mea illum, ludus solet idpro.</p></div>
  <div class="foot"><div class="rule"></div><span class="cr">BE © Brisco Energy. All rights reserved</span><span class="pg">8</span></div>
</section>

<!-- 10 chart -->
<section class="slide c1 r4">
  <div class="logo">Brisco Energy</div>
  <div class="abs" style="left:22px;top:18px;font:700 15px/1.3 'Poppins',sans-serif;color:var(--navy)">Market<br>Opportunities.</div>
  <div class="abs" style="left:0;top:88px;width:170px;height:137px;background:var(--soft)"></div>
  <div class="abs" style="left:25px;top:100px;width:125px">
    <div class="h" style="font-size:7px"><span style="display:inline-block;width:5px;height:5px;border-radius:50%;background:var(--blue);margin-right:6px"></span>Lorem Ipsum</div><p class="p" style="margin:1px 0 10px 12px">Lorem ipsum dolor sit amet, consectetuer adipiscing elit, sed diam nonummy nibh euismod tincidunt ut laoreet</p>
    <div class="h" style="font-size:7px"><span style="display:inline-block;width:5px;height:5px;border-radius:50%;background:var(--blue);margin-right:6px"></span>Lorem Ipsum</div><p class="p" style="margin:1px 0 10px 12px">Lorem ipsum dolor sit amet, consectetuer adipiscing elit, sed diam nonummy nibh euismod tincidunt ut laoreet</p>
    <div class="h" style="font-size:7px"><span style="display:inline-block;width:5px;height:5px;border-radius:50%;background:var(--blue);margin-right:6px"></span>Lorem Ipsum</div><p class="p" style="margin:1px 0 0 12px">Lorem ipsum dolor sit amet, consectetuer adipiscing elit, sed diam nonummy nibh euismod tincidunt ut laoreet</p>
  </div>
  <svg class="abs" style="left:180px;top:60px" width="300" height="190" viewBox="0 0 300 190">
    <line x1="10" y1="151" x2="295" y2="151" stroke="#ccc" stroke-width=".6"/>
    <g font-family="Open Sans,sans-serif" font-size="5" fill="#555" text-anchor="middle">
      <rect x="21" y="31" width="7" height="120" fill="var(--navy)"/><rect x="33" y="84" width="7" height="67" fill="var(--blue)"/><rect x="45" y="95" width="7" height="56" fill="#d2d3d6"/>
      <text x="24" y="28">43%</text><text x="36" y="81">24%</text><text x="48" y="92">20%</text><text x="38" y="164">1</text>
      <rect x="94" y="28" width="7" height="123" fill="var(--navy)"/><rect x="106" y="81" width="7" height="70" fill="var(--blue)"/><rect x="118" y="95" width="7" height="56" fill="#d2d3d6"/>
      <text x="97" y="25">44%</text><text x="109" y="78">25%</text><text x="121" y="92">20%</text><text x="111" y="164">2</text>
      <rect x="167" y="53" width="7" height="98" fill="var(--navy)"/><rect x="179" y="101" width="7" height="50" fill="var(--blue)"/><rect x="191" y="67" width="7" height="84" fill="#d2d3d6"/>
      <text x="170" y="50">35%</text><text x="182" y="98">18%</text><text x="194" y="64">30%</text><text x="184" y="164">3</text>
      <rect x="240" y="25" width="7" height="126" fill="var(--navy)"/><rect x="252" y="73" width="7" height="78" fill="var(--blue)"/><rect x="264" y="11" width="7" height="140" fill="#d2d3d6"/>
      <text x="243" y="22">45%</text><text x="255" y="70">28%</text><text x="267" y="8">50%</text><text x="258" y="164">4</text>
    </g>
    <g font-family="Open Sans,sans-serif" font-size="4" fill="#333"><rect x="100" y="174" width="3" height="3" fill="var(--navy)"/><text x="105" y="177">Series1</text><rect x="132" y="174" width="3" height="3" fill="var(--blue)"/><text x="137" y="177">Series2</text><rect x="164" y="174" width="3" height="3" fill="#d2d3d6"/><text x="169" y="177">Series3</text></g>
  </svg>
  <div class="foot"><div class="rule"></div><span class="cr">BE © Brisco Energy. All rights reserved</span><span class="pg">9</span></div>
</section>

<!-- 11 -->
<section class="slide c2 r4">
  <div class="ttl">Text Added Hare</div><div class="logo">Brisco Energy</div>
  <div class="photo" role="img" aria-label="Faint world map in the background" style="left:60px;top:45px;width:370px;height:160px;background:radial-gradient(ellipse at center,#f2f3f6 0%,#fff 70%)"></div>
  <div class="abs" style="left:58px;top:80px;width:70px;height:105px;border:1.5px solid var(--navy);padding:18px 6px 0"><div class="h" style="font-size:6px">Lorem ipsum</div><p class="p" style="font-size:3.4px">ipsum dolor sit amet, cons ectetuer adipiscing elit, sed diam nonummy nibh euismod tincidunt ut laoreet<br><br>ipsum dolor sit amet, cons ectetuer adipiscing elit, sed diam nonummy nibh euismod tincidunt ut laoreet ipsum dolor sit amet</p></div>
  <div class="abs" style="left:153px;top:80px;width:70px;height:105px;border:1.5px solid var(--navy);padding:18px 6px 0"><div class="h" style="font-size:6px">Lorem ipsum</div><p class="p" style="font-size:3.4px">ipsum dolor sit amet, cons ectetuer adipiscing elit, sed diam nonummy nibh euismod tincidunt ut laoreet<br><br>ipsum dolor sit amet, cons ectetuer adipiscing elit, sed diam nonummy nibh euismod tincidunt ut laoreet dolor sit</p></div>
  <div class="abs" style="left:248px;top:80px;width:70px;height:105px;border:1.5px solid var(--navy);padding:18px 6px 0"><div class="h" style="font-size:6px">Lorem ipsum</div><p class="p" style="font-size:3.4px">ipsum dolor sit amet, cons ectetuer adipiscing elit, sed diam nonummy nibh euismod tincidunt ut laoreet<br><br>ipsum dolor sit amet, cons ectetuer adipiscing elit, sed diam nonummy nibh euismod tincidunt ut laoreet ipsum</p></div>
  <div class="abs" style="left:343px;top:80px;width:80px;height:105px;border:1.5px solid var(--navy);padding:18px 6px 0"><div class="h" style="font-size:6px">Lorem ipsum</div><p class="p" style="font-size:3.4px">ipsum dolor sit amet, cons ectetuer adipiscing elit, sed diam nonummy nibh euismod tincidunt ut laoreet<br><br>ipsum dolor sit amet, cons ectetuer adipiscing elit, sed diam nonummy nibh euismod tincidunt ut laoreet</p></div>
  <div class="dot" style="left:85px;top:64px;width:18px;height:18px;border:2px solid #fff;box-shadow:0 0 0 1px var(--blue)"><i style="width:7px;height:7px;border:1.2px solid #fff"></i></div>
  <div class="dot" style="left:180px;top:64px;width:18px;height:18px;border:2px solid #fff;box-shadow:0 0 0 1px var(--blue)"><i style="width:7px;height:7px;border:1.2px solid #fff;border-radius:50%"></i></div>
  <div class="dot" style="left:275px;top:64px;width:18px;height:18px;border:2px solid #fff;box-shadow:0 0 0 1px var(--blue)"><i style="width:7px;height:7px;border:1.2px solid #fff"></i></div>
  <div class="dot" style="left:374px;top:64px;width:18px;height:18px;border:2px solid #fff;box-shadow:0 0 0 1px var(--blue)"><i style="width:8px;height:6px;border:1.2px solid #fff"></i></div>
  <div class="abs" style="left:58px;top:200px;font:600 13px 'Poppins',sans-serif;color:var(--blue)">+ 35k</div>
  <p class="abs p" style="left:58px;top:218px;width:290px">Lorem ipsum dolor sit amet, consectetuer adipiscing elit, sed diam nonummy nibh euismod tincidunt ut laoreet dolore magna aliquam erat volutpat. Ut wisi enim ad minim veniam, quis nostrud exerci tation ullamcorper.</p>
  <div class="foot"><div class="rule"></div><span class="cr">BE © Brisco Energy. All rights reserved</span><span class="pg">10</span></div>
</section>

<!-- 12 grid -->
<section class="slide c3 r4">
  <div class="ttl">Text Added Hare</div><div class="logo">Brisco Energy</div>
  <div class="abs" style="left:22px;top:64px;width:455px;display:grid;grid-template-columns:repeat(3,1fr);column-gap:14px;row-gap:18px">
    <div><div class="h">1. Text Added Here</div><p class="p" style="font-size:3.5px;text-align:justify">Lorem ipsum dolor sit amet, cons ectetuer adipiscing elit, sed diam nonummy nibh euismod tincidunt ut laoreet dolore magna aliquam erat volutpat. Ut wisi enim ad minim veniam, quis nostrud exerci tation ullamcorper suscipit lobortis nisl ut aliquip ex ea commodo consequat.<br><br>Lorem ipsum dolor sit amet, consectetuer adipiscing elit, sed diam nonummy nibh euismod tincidunt ut laoreet.</p></div>
    <div><div class="hb">1. Text Added Here</div><p class="p" style="font-size:3.5px;text-align:justify">Lorem ipsum dolor sit amet, cons ectetuer adipiscing elit, sed diam nonummy nibh euismod tincidunt ut laoreet dolore magna aliquam erat volutpat. Ut wisi enim ad minim veniam, quis nostrud exerci tation.<br><br>Lorem ipsum dolor sit amet, consectetuer adipiscing elit, sed diam nonummy nibh euismod tincidunt ut laoreet dolore magna aliquam erat volutpat. Ut wisi enim ad minim veniam.</p></div>
    <div><div class="h">1. Text Added Here</div><p class="p" style="font-size:3.5px;text-align:justify">Lorem ipsum dolor sit amet, cons ectetuer adipiscing elit, sed diam nonummy nibh euismod tincidunt ut laoreet dolore magna aliquam erat volutpat.<br><br>Lorem ipsum dolor sit amet, consectetuer adipiscing elit, sed diam nonummy nibh euismod tincidunt ut laoreet dolore magna aliquam erat volutpat. Ut wisi enim ad minim veniam, quis nostrud.</p></div>
    <div><div class="hb">1. Text Added Here</div><p class="p" style="font-size:3.5px;text-align:justify">Lorem ipsum dolor sit amet, cons ectetuer adipiscing elit, sed diam nonummy nibh euismod tincidunt ut laoreet dolore magna aliquam erat volutpat. Ut wisi enim ad minim veniam.<br><br>Lorem ipsum dolor sit amet, consectetuer adipiscing elit, sed diam nonummy nibh euismod tincidunt ut laoreet dolore magna.</p></div>
    <div><div class="h">1. Text Added Here</div><p class="p" style="font-size:3.5px;text-align:justify">Lorem ipsum dolor sit amet, cons ectetuer adipiscing elit, sed diam nonummy nibh euismod tincidunt ut laoreet dolore magna aliquam erat volutpat. Ut wisi enim ad minim veniam.<br><br>Lorem ipsum dolor sit amet, consectetuer adipiscing elit, sed diam nonummy nibh euismod tincidunt ut laoreet dolore magna aliquip ex ea commodo consequat.</p></div>
    <div><div class="hb">1. Text Added Here</div><p class="p" style="font-size:3.5px;text-align:justify">Lorem ipsum dolor sit amet, cons ectetuer adipiscing elit, sed diam nonummy nibh euismod tincidunt ut laoreet dolore magna aliquam erat volutpat.<br><br>Lorem ipsum dolor sit amet, consectetuer adipiscing elit, sed diam nonummy nibh euismod tincidunt ut laoreet dolore magna aliquam erat volutpat.</p></div>
  </div>
  <div class="foot"><div class="rule"></div><span class="cr">BE © Brisco Energy. All rights reserved</span><span class="pg">11</span></div>
</section>

<!-- 13 options -->
<section class="slide c1 r5">
  <div class="ttl">Text Added Hare</div><div class="logo">Brisco Energy</div>
  <svg class="abs" style="left:30px;top:110px" width="55" height="55" viewBox="0 0 55 55"><path d="M0 0h25l28 27-28 28H0l28-28z" fill="#ececee"/></svg>
  <div class="photo" role="img" aria-label="Photo of a small car charging at a street charger" style="left:110px;top:58px;width:92px;height:110px;background:linear-gradient(170deg,#b9c0c8,#6d7a87 60%,#495866)"></div>
  <div class="photo" role="img" aria-label="Photo of an EV charging plug close-up" style="left:220px;top:58px;width:92px;height:110px;background:linear-gradient(170deg,#9fc3ea,#d7e3ee 55%,#7d95ad)"></div>
  <div class="photo" role="img" aria-label="Photo of a charging station beside a blue car" style="left:330px;top:58px;width:92px;height:110px;background:linear-gradient(170deg,#4a4f57,#6b7886 55%,#7fb1d8)"></div>
  <div class="abs" style="left:110px;top:165px;width:92px;height:3px;background:var(--blue)"></div>
  <div class="abs" style="left:220px;top:165px;width:92px;height:3px;background:var(--blue)"></div>
  <div class="abs" style="left:330px;top:165px;width:92px;height:3px;background:var(--blue)"></div>
  <div class="abs" style="left:110px;top:172px;width:88px"><div style="font:500 7px 'Poppins',sans-serif;color:var(--blue)">First <b style="color:var(--navy)">Option</b></div><p class="p">Lorem ipsum dolor sit consectetuer adipiscing elit, sed diam nonummy nibh euismod tincidunt ut dolore magna aliquam erat volutpat. Ut wisi enim ad minim veniam, quis nostrud</p></div>
  <div class="abs" style="left:220px;top:172px;width:88px"><div style="font:500 7px 'Poppins',sans-serif;color:var(--blue)">Second <b style="color:var(--navy)">Option</b></div><p class="p">Lorem ipsum dolor sit consectetuer adipiscing elit, sed diam nonummy nibh euismod tincidunt ut dolore magna aliquam erat volutpat. Ut wisi enim ad minim veniam, quis nostrud</p></div>
  <div class="abs" style="left:330px;top:172px;width:88px"><div style="font:500 7px 'Poppins',sans-serif;color:var(--blue)">Third <b style="color:var(--navy)">Option</b></div><p class="p">Lorem ipsum dolor sit consectetuer adipiscing elit, sed diam nonummy nibh euismod tincidunt ut dolore magna aliquam erat volutpat. Ut wisi enim ad minim veniam, quis nostrud</p></div>
  <div class="foot"><div class="rule"></div><span class="cr">BE © Brisco Energy. All rights reserved</span><span class="pg">12</span></div>
</section>

<!-- 14 hub -->
<section class="slide c2 r5">
  <div class="ttl">Text Added Hare</div><div class="logo">Brisco Energy</div>
  <svg class="abs" style="left:40px;top:60px" width="230" height="150" viewBox="0 0 230 150">
    <circle cx="60" cy="75" r="57" fill="none" stroke="var(--navy)" stroke-width="2"/>
    <circle cx="60" cy="75" r="50" fill="var(--navy)"/>
    <circle cx="60" cy="75" r="44" fill="none" stroke="#fff" stroke-width="1"/>
    <text x="60" y="78" text-anchor="middle" font-family="Poppins,sans-serif" font-weight="700" font-size="9" fill="#fff">Brisco Energy</text>
    <path d="M133 40l12-18h48 M128 75h65 M133 110l12 18h48" fill="none" stroke="var(--navy)" stroke-width="1.2"/>
  </svg>
  <div class="dot" style="left:243px;top:73px;width:26px;height:26px"><i style="width:11px;height:11px;border:1.5px solid #fff;border-radius:50%"></i></div>
  <div class="dot" style="left:243px;top:123px;width:26px;height:26px"><i style="width:11px;height:11px;border:1.5px solid #fff;border-radius:50%"></i></div>
  <div class="dot" style="left:243px;top:176px;width:26px;height:26px"><i style="width:11px;height:11px;border:1.5px solid #fff;border-radius:50%"></i></div>
  <div class="abs" style="left:291px;top:70px;width:160px"><div class="h" style="font-size:7.5px">Project name</div><p class="p">Lorem ipsum dolor sit amet, nec an dictas equidem appellantur, ut has commune accommodare. Mea illum, ludus solet idpro.</p></div>
  <div class="abs" style="left:291px;top:120px;width:160px"><div class="h" style="font-size:7.5px">Project name</div><p class="p">Lorem ipsum dolor sit amet, nec an dictas equidem appellantur, ut has commune accommodare. Mea illum, ludus solet idpro.</p></div>
  <div class="abs" style="left:291px;top:174px;width:160px"><div class="h" style="font-size:7.5px">Project name</div><p class="p">Lorem ipsum dolor sit amet, nec an dictas equidem appellantur, ut has commune accommodare. Mea illum, ludus solet idpro.</p></div>
  <div class="foot"><div class="rule"></div><span class="cr">BE © Brisco Energy. All rights reserved</span><span class="pg">13</span></div>
</section>

<!-- 15 donuts -->
<section class="slide c3 r5">
  <div class="ttl">Text Added Hare</div><div class="logo">Brisco Energy</div>
  <p class="abs p" style="left:22px;top:45px;width:430px;font-size:4.6px">Lorem ipsum dolor sit amet, consectetuer adipiscing elit, sed diam nonummy nibh euismod tincidunt ut laoreet dolore magna aliquam erat volutpat. Ut wisi enim ad minim veniam, quis nostrud exerci tation ullamcorper suscipit lobortis nisl ut aliquip ex ea commodo consequat. Duis autem vel eum iriure</p>
  <svg class="abs" style="left:50px;top:95px" width="400" height="140" viewBox="0 0 400 140">
    <g fill="none" stroke-width="6" transform="rotate(-90)">
      <circle cx="-57" cy="60" r="40" stroke="#e6e7ea"/><circle cx="-57" cy="60" r="40" stroke="var(--navy)" stroke-dasharray="125.7 251.3"/>
      <circle cx="-57" cy="193" r="40" stroke="#e6e7ea"/><circle cx="-57" cy="193" r="40" stroke="var(--blue)" stroke-dasharray="188.5 251.3"/>
      <circle cx="-57" cy="322" r="40" stroke="#e6e7ea"/><circle cx="-57" cy="322" r="40" stroke="#c6c7cb" stroke-dasharray="100.5 251.3"/>
    </g>
    <g font-family="Poppins,sans-serif" font-size="20" font-weight="600" fill="#1a1a2a" text-anchor="middle"><text x="60" y="64">50%</text><text x="193" y="64">75%</text><text x="322" y="64">40%</text></g>
    <g font-family="Open Sans,sans-serif" font-size="4.5" fill="#777" text-anchor="middle"><text x="60" y="114">Lorem ipsum dolor amet amet</text><text x="60" y="120">consectetur dolor</text><text x="193" y="114">Lorem ipsum dolor amet amet</text><text x="193" y="120">consectetur dolor</text><text x="322" y="114">Lorem ipsum dolor amet amet</text><text x="322" y="120">consectetur dolor</text></g>
  </svg>
  <div class="foot"><div class="rule"></div><span class="cr">BE © Brisco Energy. All rights reserved</span><span class="pg">14</span></div>
</section>

<!-- 16 timeline -->
<section class="slide c1 r6">
  <div class="ttl">Text Added Hare</div><div class="logo">Brisco Energy</div>
  <svg class="abs" style="left:50px;top:70px" width="400" height="130" viewBox="0 0 400 130">
    <g fill="var(--navy)"><path d="M12 60h70l4 5-4 5H12l-4-5z"/><path d="M170 60h70l4 5-4 5h-70l-4-5z"/><path d="M330 60h46l4 5-4 5h-46l-4-5z"/></g>
    <g fill="var(--blue)"><path d="M92 60h70l4 5-4 5H92l-4-5z"/><path d="M250 60h70l4 5-4 5h-70l-4-5z"/></g>
    <g font-family="Poppins,sans-serif" font-size="5" font-weight="600" fill="#fff" text-anchor="middle"><text x="47" y="67">1990</text><text x="127" y="67">2001</text><text x="207" y="67">2007</text><text x="287" y="67">2012</text><text x="353" y="67">2020</text></g>
    <g stroke="var(--navy)" stroke-width="1"><line x1="70" y1="40" x2="70" y2="57"/><line x1="230" y1="40" x2="230" y2="57"/><line x1="376" y1="40" x2="376" y2="57"/><line x1="150" y1="73" x2="150" y2="90" stroke="var(--blue)"/><line x1="310" y1="73" x2="310" y2="90" stroke="var(--blue)"/></g>
    <g fill="var(--navy)"><circle cx="70" cy="39" r="2"/><circle cx="230" cy="39" r="2"/><circle cx="376" cy="39" r="2"/></g>
    <g fill="var(--blue)"><circle cx="150" cy="90" r="2"/><circle cx="310" cy="90" r="2"/></g>
    <g font-family="Poppins,sans-serif" font-size="5.5" font-weight="500" fill="var(--blue)" text-anchor="middle"><text x="70" y="10">Your Title</text><text x="230" y="10">Your Title</text><text x="376" y="10">Your Title</text></g>
    <g font-family="Poppins,sans-serif" font-size="5.5" font-weight="600" fill="var(--navy)" text-anchor="middle"><text x="150" y="104">Your Title</text><text x="310" y="104">Your Title</text></g>
    <g font-family="Open Sans,sans-serif" font-size="4" fill="#666" text-anchor="middle"><text x="70" y="17">Refers to a good or</text><text x="70" y="22">service being offered</text><text x="230" y="17">Refers to a good or</text><text x="230" y="22">service being offered</text><text x="376" y="17">Refers to a good or</text><text x="376" y="22">service being offered</text><text x="150" y="111">Refers to a good or</text><text x="150" y="116">service being offered</text><text x="310" y="111">Refers to a good or</text><text x="310" y="116">service being offered</text></g>
  </svg>
  <div class="foot"><div class="rule"></div><span class="cr">BE © Brisco Energy. All rights reserved</span><span class="pg">15</span></div>
</section>

<!-- 17 quadrant -->
<section class="slide c2 r6">
  <div class="ttl">Text Added Hare</div><div class="logo">Brisco Energy</div>
  <svg class="abs" style="left:175px;top:70px" width="140" height="140" viewBox="0 0 140 140">
    <g transform="translate(70 70)">
      <path d="M2 -65A65 65 0 0 1 65 -2H30A30 30 0 0 0 2 -30Z" fill="var(--blue)"/>
      <path d="M65 2A65 65 0 0 1 2 65V30A30 30 0 0 0 30 2Z" fill="var(--navy)"/>
      <path d="M-2 65A65 65 0 0 1 -65 2H-30A30 30 0 0 0 -2 30Z" fill="var(--blue)"/>
      <path d="M-65 -2A65 65 0 0 1 -2 -65V-30A30 30 0 0 0 -30 -2Z" fill="var(--navy)"/>
      <circle r="28" fill="#fff"/>
      <g fill="#fff" stroke="none"><circle cx="38" cy="-38" r="6"/><circle cx="38" cy="38" r="6"/><circle cx="-38" cy="38" r="6"/><circle cx="-38" cy="-38" r="6"/></g>
      <text y="-2" text-anchor="middle" font-family="Poppins,sans-serif" font-size="11" font-weight="600" fill="#333">Text</text>
      <text y="11" text-anchor="middle" font-family="Poppins,sans-serif" font-size="11" font-weight="600" fill="#333">Added</text>
    </g>
  </svg>
  <div class="abs" style="left:30px;top:68px;width:135px;text-align:right"><div class="h" style="color:#444">Text Here</div><p class="p">Lorem ipsum dolor sit amet, consectetuer adipiscing elit, sed diammy nibh euismod tincidunt ut laoreet dolore</p></div>
  <div class="abs" style="left:30px;top:160px;width:135px;text-align:right"><div class="h" style="color:#444">Text Here</div><p class="p">Lorem ipsum dolor sit amet, consectetuer adipiscing elit, sed diammy nibh euismod tincidunt ut laoreet dolore</p></div>
  <div class="abs" style="left:328px;top:68px;width:135px"><div class="h" style="color:#444">Text Here</div><p class="p">Lorem ipsum dolor sit amet, consectetuer adipiscing elit, sed diammy nibh euismod tincidunt ut laoreet dolore</p></div>
  <div class="abs" style="left:328px;top:160px;width:135px"><div class="h" style="color:#444">Text Here</div><p class="p">Lorem ipsum dolor sit amet, consectetuer adipiscing elit, sed diammy nibh euismod tincidunt ut laoreet dolore</p></div>
  <div class="foot"><div class="rule"></div><span class="cr">BE © Brisco Energy. All rights reserved</span><span class="pg">16</span></div>
</section>

<!-- 18 steps -->
<section class="slide c3 r6">
  <div class="ttl">Text Added Hare</div><div class="logo">Brisco Energy</div>
  <svg class="abs" style="left:30px;top:70px" width="440" height="120" viewBox="0 0 440 120">
    <path d="M5 61H400" stroke="var(--navy)" stroke-width="4"/>
    <path d="M330 61H430" stroke="var(--blue)" stroke-width="4"/><path d="M428 55l8 6-8 6z" fill="var(--blue)"/>
    <g><circle cx="83" cy="35" r="23" fill="none" stroke="var(--navy)" stroke-width="4"/><circle cx="83" cy="35" r="16" fill="#fff" stroke="var(--navy)" stroke-width="2"/><path d="M83 27v8l5 4" stroke="var(--navy)" fill="none" stroke-width="1.5"/>
      <circle cx="170" cy="35" r="23" fill="none" stroke="var(--blue)" stroke-width="4"/><circle cx="170" cy="35" r="16" fill="var(--navy)"/><text x="170" y="39" text-anchor="middle" font-size="10" font-family="Poppins,sans-serif" fill="#fff">$</text>
      <circle cx="256" cy="35" r="23" fill="none" stroke="var(--navy)" stroke-width="4"/><circle cx="256" cy="35" r="16" fill="#fff" stroke="var(--navy)" stroke-width="2"/><path d="M249 30h14M249 35h14M249 40h14" stroke="var(--navy)" stroke-width="2.5"/>
      <circle cx="343" cy="35" r="23" fill="none" stroke="var(--blue)" stroke-width="4"/><circle cx="343" cy="35" r="16" fill="#fff" stroke="var(--blue)" stroke-width="2"/><circle cx="345" cy="32" r="5" fill="none" stroke="var(--navy)" stroke-width="1.5"/><path d="M341 36l-5 5" stroke="var(--navy)" stroke-width="2"/></g>
    <g font-family="Poppins,sans-serif" font-size="4.5" fill="#fff" text-anchor="middle"><rect x="70" y="58" width="26" height="6" fill="var(--navy)"/><text x="83" y="62.5">Step 01</text><rect x="157" y="58" width="26" height="6" fill="var(--blue)"/><text x="170" y="62.5">Step 02</text><rect x="243" y="58" width="26" height="6" fill="var(--navy)"/><text x="256" y="62.5">Step 03</text><rect x="355" y="58" width="26" height="6" fill="var(--blue)"/><text x="368" y="62.5">Step 04</text></g>
    <g stroke="#888" stroke-width=".8"><line x1="83" y1="68" x2="83" y2="80"/><line x1="170" y1="68" x2="170" y2="80"/><line x1="256" y1="68" x2="256" y2="80"/><line x1="343" y1="68" x2="343" y2="80"/></g>
    <g font-family="Poppins,sans-serif" font-size="7" font-weight="500" fill="var(--navy)" text-anchor="middle"><text x="83" y="92">Lorem Ipsum</text><text x="170" y="92">Lorem Ipsum</text><text x="256" y="92">Lorem Ipsum</text><text x="343" y="92">Lorem Ipsum</text></g>
    <g font-family="Open Sans,sans-serif" font-size="3.5" fill="#777" text-anchor="middle"><text x="83" y="99">Lorem ipsum dolor sit amet,</text><text x="83" y="104">consectetuer adipiscing elit, sed</text><text x="83" y="109">nibh euismod tincidunt ut</text><text x="170" y="99">Lorem ipsum dolor sit amet,</text><text x="170" y="104">consectetuer adipiscing elit, sed</text><text x="170" y="109">nibh euismod tincidunt ut</text><text x="256" y="99">Lorem ipsum dolor sit amet,</text><text x="256" y="104">consectetuer adipiscing elit, sed</text><text x="256" y="109">nibh euismod tincidunt ut</text><text x="343" y="99">Lorem ipsum dolor sit amet,</text><text x="343" y="104">consectetuer adipiscing elit, sed</text><text x="343" y="109">nibh euismod tincidunt ut</text></g>
  </svg>
  <div class="foot"><div class="rule"></div><span class="cr">BE © Brisco Energy. All rights reserved</span><span class="pg">17</span></div>
</section>

<!-- 19 phones -->
<section class="slide c1 r7">
  <div class="ttl">Text Added Hare</div><div class="logo">Brisco Energy</div>
  <p class="abs p" style="left:25px;top:50px;width:150px;font-size:4.6px">Lorem ipsum dolor sit amet, consectetuer adipiscing elit, sed diam nonummy nibh euismod tincidunt ut laoreet dolore magna aliquam erat volutpat. Ut wisi enim ad minim veniam,<br><br>quis nostrud exerci tation ullamcorper suscipit lobortis nisl ut aliquip ex ea commodo consequat. Duis autem vel eum iriure dolor in hendrerit in vulputate velit esse</p>
  <div class="abs" style="left:25px;top:150px;width:150px">
    <div style="display:flex;gap:6px;margin-bottom:8px"><span style="width:12px;height:12px;background:var(--blue);color:#fff;font:700 8px/12px Poppins,sans-serif;text-align:center">1.</span><div><div class="h">Lorem ipsum</div><p class="p" style="font-size:3.5px">Lorem ipsum dolor sit amet, consectetuer adipiscing elit, sed diam nonummy nibh euismod tincid</p></div></div>
    <div style="display:flex;gap:6px;margin-bottom:8px"><span style="width:12px;height:12px;background:var(--blue);color:#fff;font:700 8px/12px Poppins,sans-serif;text-align:center">2.</span><div><div class="h">Lorem ipsum</div><p class="p" style="font-size:3.5px">Lorem ipsum dolor sit amet, consectetuer adipiscing elit, sed diam nonummy nibh euismod tincid</p></div></div>
    <div style="display:flex;gap:6px"><span style="width:12px;height:12px;background:var(--blue);color:#fff;font:700 8px/12px Poppins,sans-serif;text-align:center">3.</span><div><div class="h">Lorem ipsum</div><p class="p" style="font-size:3.5px">Lorem ipsum dolor sit amet, consectetuer adipiscing elit, sed diam nonummy nibh euismod tincid</p></div></div>
  </div>
  <div class="abs" style="left:228px;top:20px;width:57px;height:115px;border:2.5px solid #222;border-radius:6px;background:#fff;padding:12px 5px"><div class="h" style="font-size:5.5px">Lorem<br>ipsum dolor</div><div style="width:12px;height:9px;border:1px solid var(--blue);margin:14px auto 6px"></div><p class="p" style="font-size:2.8px;text-align:center">Its introduce the students to the changing landscape of marketing and equip them with knowledge and skills</p></div>
  <div class="abs" style="left:301px;top:62px;width:57px;height:115px;border:2.5px solid #222;border-radius:6px;background:#fff;padding:12px 5px"><div class="h" style="font-size:5.5px">Dolor sit<br>amet, conse</div><div style="width:12px;height:9px;border:1px solid var(--blue);margin:6px auto 8px"></div><p class="p" style="font-size:2.8px;text-align:center">You will learn concepts and ideas in digital marketing as well as how to use different tools and strategies</p></div>
  <div class="abs" style="left:374px;top:100px;width:57px;height:115px;border:2.5px solid #222;border-radius:6px;background:#fff;padding:12px 5px"><div class="h" style="font-size:5.5px">Consec</div><div style="width:12px;height:12px;border:1px solid var(--blue);border-radius:50%;margin:16px auto 8px"></div><p class="p" style="font-size:2.8px;text-align:center">You are required to pass 80% of the evaluation test to obtain the certificate</p></div>
  <div class="foot"><div class="rule"></div><span class="cr">BE © Brisco Energy. All rights reserved</span><span class="pg">17</span></div>
</section>

<!-- 20 team -->
<section class="slide c2 r7">
  <div class="ttl">Text Added Hare</div><div class="logo">Brisco Energy</div>
  <div class="abs" style="left:45px;top:85px;width:72px;height:22px;background:var(--blue)"></div>
  <div class="abs" style="left:152px;top:85px;width:72px;height:22px;background:var(--navy)"></div>
  <div class="abs" style="left:262px;top:85px;width:72px;height:22px;background:var(--blue)"></div>
  <div class="abs" style="left:373px;top:85px;width:72px;height:22px;background:var(--navy)"></div>
  <div class="photo" role="img" aria-label="Team member portrait" style="left:63px;top:92px;width:36px;height:36px;border-radius:50%;border:2px solid #fff;background:linear-gradient(160deg,#d9dbe0,#9ea3ab)"></div>
  <div class="photo" role="img" aria-label="Team member portrait" style="left:170px;top:92px;width:36px;height:36px;border-radius:50%;border:2px solid #fff;background:linear-gradient(160deg,#d9dbe0,#9ea3ab)"></div>
  <div class="photo" role="img" aria-label="Team member portrait" style="left:280px;top:92px;width:36px;height:36px;border-radius:50%;border:2px solid #fff;background:linear-gradient(160deg,#d9dbe0,#9ea3ab)"></div>
  <div class="photo" role="img" aria-label="Team member portrait" style="left:391px;top:92px;width:36px;height:36px;border-radius:50%;border:2px solid #fff;background:linear-gradient(160deg,#d9dbe0,#9ea3ab)"></div>
  <div class="abs" style="left:40px;top:137px;width:82px;text-align:center"><div class="h" style="font-size:7px">EVAN HALE</div><p class="p" style="font-size:3.5px">ipsum dolor sit amet, cons ectetuer adipiscing elit, sed diam nonummy nibh euismod tincid<br><br>aliquam erat volutpat. Ut wisi enim ad minim veniam, quis nostrud</p></div>
  <div class="abs" style="left:147px;top:137px;width:82px;text-align:center"><div class="h" style="font-size:7px">NORA QUINN</div><p class="p" style="font-size:3.5px">ipsum dolor sit amet, cons ectetuer adipiscing elit, sed diam nonummy nibh euismod tincid<br><br>aliquam erat volutpat. Ut wisi enim ad minim veniam, quis nostrud</p></div>
  <div class="abs" style="left:257px;top:137px;width:82px;text-align:center"><div class="h" style="font-size:7px">EVAN HALE</div><p class="p" style="font-size:3.5px">ipsum dolor sit amet, cons ectetuer adipiscing elit, sed diam nonummy nibh euismod tincid<br><br>Ut wisi enim ad minim veniam, quis nostrud</p></div>
  <div class="abs" style="left:368px;top:137px;width:82px;text-align:center"><div class="h" style="font-size:7px">NORA QUINN</div><p class="p" style="font-size:3.5px">ipsum dolor sit amet, cons ectetuer adipiscing elit, sed diam nonummy nibh euismod tincid<br><br>aliquam erat volutpat. Ut wisi enim ad minim veniam, quis nostrud</p></div>
  <div class="foot"><div class="rule"></div><span class="cr">BE © Brisco Energy. All rights reserved</span><span class="pg">17</span></div>
</section>

<!-- 21 thank you -->
<section class="slide c3 r7" style="background:linear-gradient(135deg,#fff 40%,#f0f1f3)">
  <div class="photo" role="img" aria-label="Photo of a white electric car plugged into a wall charger" style="left:0;top:20px;width:265px;height:236px;background:linear-gradient(120deg,#cfd3da 0%,#eef0f3 45%,#b6bcc5 100%)"></div>
  <div class="abs" style="left:52px;top:10px;width:153px;height:7px;background:var(--navy-deep)"></div>
  <div class="abs" style="left:52px;top:259px;width:153px;height:7px;background:var(--navy-deep)"></div>
  <div class="abs" style="left:200px;top:225px;font:700 6px 'Poppins',sans-serif;color:var(--navy);background:#fff;padding:2px 4px">Brisco Energy</div>
  <div class="abs" style="left:280px;top:35px;font:700 29px 'Oswald',sans-serif;color:var(--navy-deep)">Thank You</div>
  <svg class="abs" style="left:283px;top:90px" width="14" height="110" viewBox="0 0 14 110">
    <path d="M3 2c2-1 3 0 4 3l-1 2c1 2 2 3 4 4l2-1c3 1 4 2 3 4-1 2-3 3-6 1C5 13 2 9 2 6c0-2 0-3 1-4z" fill="var(--blue)"/>
    <path d="M1 53 13 47 8 60 6 55z" fill="var(--blue)"/>
    <path d="M1 90l6-6 6 6h-2v7H9v-4H5v4H3v-7z" fill="var(--blue)"/>
  </svg>
  <div class="abs" style="left:305px;top:88px;width:1px;height:16px;background:#333"></div>
  <div class="abs" style="left:305px;top:132px;width:1px;height:16px;background:#333"></div>
  <div class="abs" style="left:305px;top:172px;width:1px;height:16px;background:#333"></div>
  <div class="abs" style="left:312px;top:87px;font-size:6px;line-height:1.35;color:#333">+18 0000 1111 2222<br>+18 0000 1111 2222</div>
  <div class="abs" style="left:312px;top:131px;font-size:6px;line-height:1.35;color:#333">www.websitename.com<br>uname@email.com</div>
  <div class="abs" style="left:312px;top:171px;font-size:6px;line-height:1.35;color:#333">1234 Street name, town/city,<br>state/country, post/zip 000000.</div>
</section>

</div>
</body>
</html>
```